Glamour By Tavi

I am a makeup artist looking for professional looking double sided business card. I would like to create a logo and incorporate a set of eyes as the periods above the name "Tavi" on the card.

front of card: Logo "Glamour by Tavi" written across diagonal (bottom left to top right)

Back of card:
1) Professional makeup artist serving New York & New Jersey (or similar to this text)
2) 917-555-0148
3) glamourbytavi@mailcove.com

Industry/Entity Type

Business

```html
<!DOCTYPE html>
<html lang="en">
<head>
<meta charset="utf-8">
<title>Glamour by Tavi – Business Card</title>
<link rel="stylesheet" href="https://fonts.googleapis.com/css2?family=Delius&family=Josefin+Sans:wght@400&family=Oswald:wght@300;400&display=swap">
<style>
  :root {
    --backdrop: #858585;
    --front-light: #dfe8e6;
    --front-edge: #a9bcc0;
    --plum: #52223a;
    --ink-light: #d9e4e4;
    --shadow-yellow: #f3d67a;
    --shadow-red: #d6384a;
    --iris-teal: #3f8a8a;
  }
  * { margin: 0; padding: 0; box-sizing: border-box; }
  html, body {
    width: 1000px;
    height: 1200px;
    overflow: hidden;
    background: var(--backdrop);
  }
  .sheet {
    position: relative;
    width: 1000px;
    height: 1200px;
  }
  .card {
    position: absolute;
    left: 103px;
    width: 794px;
    height: 459px;
    overflow: hidden;
  }
  .card--front {
    top: 95px;
    background: radial-gradient(ellipse at 50% 45%, var(--front-light) 55%, var(--front-edge) 120%);
  }
  .card--back {
    top: 625px;
    background: var(--plum);
  }
  .eyes-art {
    position: absolute;
    left: 32px;
    top: 95px;
    width: 740px;
    height: 170px;
    border-radius: 60px;
    background:
      linear-gradient(90deg,
        rgba(82,34,58,0.55) 0%,
        var(--shadow-red) 12%,
        var(--shadow-yellow) 30%,
        var(--iris-teal) 40%,
        var(--shadow-yellow) 50%,
        var(--iris-teal) 68%,
        var(--shadow-yellow) 80%,
        var(--shadow-red) 90%,
        rgba(82,34,58,0.55) 100%);
    opacity: 0.85;
  }
  .wordmark {
    position: absolute;
    left: 47px;
    top: 232px;
    font-family: "Josefin Sans", sans-serif;
    font-weight: 400;
    font-size: 172px;
    line-height: 1;
    letter-spacing: 68px;
    color: var(--plum);
    white-space: nowrap;
  }
  .back-title {
    position: absolute;
    left: 57px;
    top: 44px;
    font-family: "Delius", sans-serif;
    font-weight: 400;
    font-size: 78px;
    line-height: 1.2;
    color: var(--ink-light);
    white-space: nowrap;
  }
  .back-details {
    position: absolute;
    left: 66px;
    top: 150px;
    font-family: "Oswald", sans-serif;
    font-weight: 300;
    color: var(--ink-light);
    font-size: 32px;
    line-height: 43px;
    letter-spacing: 1.5px;
  }
  .back-details p { margin-bottom: 25px; white-space: nowrap; }
  .back-details .tagline { margin-bottom: 22px; }
</style>
</head>
<body>
  <main class="sheet">
    <section class="card card--front" aria-label="Card front">
      <div class="eyes-art" role="img" aria-label="Illustration of a pair of made-up eyes with golden and red eyeshadow and arched brows, surrounded by small stars"></div>
      <h1 class="wordmark">Tavi</h1>
    </section>

    <section class="card card--back" aria-label="Card back">
      <h2 class="back-title">Glamour by Tavi</h2>
      <div class="back-details">
        <p class="tagline">Professional makeup artist serving<br>New York &amp; New Jersey</p>
        <p class="phone">917-555-0148</p>
        <p class="email">glamourbytavi@mailcove.com</p>
      </div>
    </section>
  </main>
</body>
</html>
```